New Business Card Design Project

I need a design for business cards, i am an electrical business called "Tandor Electrical and Communications" i need the cards to be double sided with the company logo on the back (attached) the front needs to say my company name, web site, email address, telephone number, and ABN number and electrical license number. I am open to different arrangements of the information but would like the background to be incorporating something electrical or something that looks smart. open to all additional ideas also.

The company colours are orange and grey see logo attached.

Business Name: Tandor Electrical and Communications
Website: tandorelectricalandcomms.example.au
Email: brent@tandorelectricalandcomms.example.au
Telephone(mobile): 0481203967
ABN: 71829034618
Lic No: 830472F

Target Market(s)

Business entities, Project Managers, Accounts, Clients

Industry/Entity Type

Electrician

Contact Information for Business Card

I need a design for business cards, i am an electrical business called "Tandor Electrical and Communications" i need the cards to be double sided with the company logo on the back (attached) the front needs to say my company name

Font styles to use
Serif
Sans Serif

Colors
f37122
5c5c5c

Requirements
Must have
• Must have the Logo on the back open to different ways of it being on the back but had in mind to keep it central but again open to other options
Nice to have
• A real modern cool background that is eye catching yet contemporary
Should not have
• No backgrounds of a light bulb or plug or anything like that

```html
<!DOCTYPE html>
<html lang="en">
<head>
<meta charset="utf-8">
<title>Tandor Electrical and Communications – Business Card</title>
<link href="https://fonts.googleapis.com/css2?family=Arimo:wght@400;700&display=swap" rel="stylesheet">
<style>
  :root {
    --orange: #f37122;
    --orange-deep: #d9590f;
    --grey: #5c5c5c;
    --charcoal-top: #4a4a4c;
    --charcoal-bottom: #1f1f21;
    --frost: #f3efec;
    --ink: #2a2a2a;
    --logo-grey: #dcdcdc;
    --backdrop: #e8e6e3;
  }
  * { margin: 0; padding: 0; box-sizing: border-box; }
  html, body {
    width: 1200px;
    height: 969px;
    overflow: hidden;
    background: var(--backdrop);
    font-family: "Arimo", Arial, sans-serif;
  }
  .business-card {
    position: absolute;
    left: 100px;
    top: 200px;
    width: 1000px;
    height: 568px;
    overflow: hidden;
    box-shadow: 0 18px 40px rgba(0,0,0,0.22);
    background: var(--frost);
  }
  .brand-panel {
    position: absolute;
    left: 0; top: 0;
    width: 100%;
    height: 342px;
    background: linear-gradient(180deg, var(--charcoal-top) 0%, #333335 45%, var(--charcoal-bottom) 100%);
    border-bottom: 5px solid var(--orange);
    display: flex;
    align-items: center;
    justify-content: center;
  }
  .brand-name {
    text-align: center;
    color: var(--logo-grey);
    font-weight: 400;
    line-height: 1;
  }
  .brand-name .brand-main {
    display: block;
    font-size: 92px;
    letter-spacing: 10px;
  }
  .brand-name .brand-sub {
    display: block;
    margin-top: 14px;
    font-size: 19px;
    letter-spacing: 3px;
  }
  .contact-panel {
    position: absolute;
    left: 0; top: 347px;
    width: 100%;
    height: 155px;
    background: linear-gradient(180deg, #faf7f4 0%, var(--frost) 60%, #ece6e1 100%);
    text-align: center;
    padding-top: 24px;
  }
  .person {
    font-size: 30px;
    color: var(--orange);
    letter-spacing: 0.5px;
  }
  .person .dash { margin: 0 12px; }
  .person .role {
    color: var(--ink);
    font-size: 25px;
  }
  .contact-row {
    margin-top: 14px;
    font-size: 25px;
    color: var(--ink);
    display: flex;
    justify-content: center;
    align-items: center;
    gap: 10px;
  }
  .contact-row + .contact-row { margin-top: 8px; }
  .contact-row .gap { width: 18px; }
  .icon { width: 22px; height: 22px; flex: none; }
  .legal-band {
    position: absolute;
    left: 0; bottom: 0;
    width: 100%;
    height: 66px;
    background: linear-gradient(180deg, var(--orange) 0%, var(--orange-deep) 100%);
    display: flex;
    align-items: center;
    justify-content: center;
    font-size: 24px;
    color: #fbe3d2;
    letter-spacing: 0.5px;
  }
  .legal-band .divider { margin: 0 12px; }
</style>
</head>
<body>
  <article class="business-card">
    <header class="brand-panel">
      <h1 class="brand-name">
        <span class="brand-main">TANDOR</span>
        <span class="brand-sub">ELECTRICAL &amp; COMMUNICATIONS</span>
      </h1>
    </header>

    <section class="contact-panel">
      <p class="person">BRENT HALLORAN<span class="dash">-</span><span class="role">PRESIDENT</span></p>
      <p class="contact-row">
        <svg class="icon" viewBox="0 0 22 22" aria-hidden="true">
          <rect x="5" y="1" width="12" height="20" rx="2" fill="none" stroke="#f37122" stroke-width="2.4"/>
          <circle cx="11" cy="17" r="1.4" fill="#f37122"/>
        </svg>
        <span>0481203967</span>
        <span class="gap"></span>
        <svg class="icon" viewBox="0 0 22 22" aria-hidden="true">
          <rect x="1" y="4" width="20" height="14" rx="1.5" fill="#f37122"/>
          <path d="M1.5 5 L11 12 L20.5 5" fill="none" stroke="#fff" stroke-width="1.6"/>
        </svg>
        <span>brent@tandorelectricalandcomms.example.au</span>
      </p>
      <p class="contact-row">
        <svg class="icon" viewBox="0 0 22 22" aria-hidden="true">
          <circle cx="11" cy="11" r="10" fill="#f37122"/>
          <path d="M1 11 H21 M11 1 C6 6 6 16 11 21 M11 1 C16 6 16 16 11 21" fill="none" stroke="#fff" stroke-width="1.3"/>
        </svg>
        <span>tandorelectricalandcomms.example.au</span>
      </p>
    </section>

    <footer class="legal-band">
      <span>ABN: 71829034618</span><span class="divider">|</span><span>Lic No: 830472F</span>
    </footer>
  </article>
</body>
</html>
```